Cover-Design für Office Notizbuch gesucht
Zielgruppe
Wir erstellen schöne Officeprodukte für junge, modebewusste (und alte) Mädels. Es soll also sehr quillorat / moranteve tauglich sein.
Aufgabenstellung
Wir möchten ein Din A5 Notizbuch haben und suchen dafür ein tolles Coverdesign.
Es soll ein zeitloses Design haben, gerne mit einem motivierenden Spruch oder einfach einem schönen Muster und Design.
Zusätzlich kann auch mit einer Heißfolienprägung Gold gearbeitet werden.

```html
<!DOCTYPE html>
<html lang="de">
<head>
<meta charset="utf-8">
<title>Notizbuch Cover – Motivation</title>
<link rel="stylesheet" href="https://fonts.googleapis.com/css2?family=Amatic+SC:wght@700&family=Caveat+Brush&display=swap">
<style>
  :root {
    --page-bg: #ffffff;
    --cover-bg: #f3f3f1;
    --ink: #3b3b3b;
    --ink-dark: #2e2e2e;
    --gold: #c9a44a;
    --leaf: #6f9a6a;
    --leaf-soft: #a9c3a2;
    --blossom: #efdcd6;
    --panel: #f7f7f5;
  }
  html, body {
    margin: 0;
    padding: 0;
    width: 1200px;
    height: 848px;
    overflow: hidden;
    background: var(--page-bg);
  }
  .canvas {
    position: relative;
    width: 1200px;
    height: 848px;
  }
  .cover {
    position: absolute;
    top: 121px;
    width: 440px;
    height: 606px;
    background: var(--cover-bg);
    box-shadow: 0 2px 10px rgba(0,0,0,0.12);
  }
  .cover--wake { left: 90px; }
  .cover--believe { left: 670px; }
  .cover-art {
    position: absolute;
    inset: 0;
    width: 440px;
    height: 606px;
  }
  .cover-quote {
    position: absolute;
    left: 110px;
    top: 200px;
    width: 220px;
    height: 200px;
    display: flex;
    flex-direction: column;
    align-items: center;
    justify-content: center;
    text-align: center;
    margin: 0;
  }
  .cover-quote--caps {
    font-family: "Amatic SC", sans-serif;
    font-weight: 700;
    font-size: 47px;
    line-height: 1.12;
    color: var(--ink);
    letter-spacing: 1px;
  }
  .cover-quote--brush {
    font-family: "Caveat Brush", cursive;
    font-size: 54px;
    line-height: 1.05;
    color: var(--ink-dark);
  }
  .quote-word--underlined {
    text-decoration: underline;
    text-decoration-thickness: 3px;
    text-underline-offset: 6px;
  }
</style>
</head>
<body>
<main class="canvas">

  <section class="cover cover--wake">
    <svg class="cover-art" viewBox="0 0 440 606" aria-hidden="false">
      <defs>
        <radialGradient id="wreath-tone-a" cx="50%" cy="50%" r="50%">
          <stop offset="55%" stop-color="#e9ede5"/>
          <stop offset="75%" stop-color="#b9cdb3"/>
          <stop offset="88%" stop-color="#e6d6d0"/>
          <stop offset="100%" stop-color="#f3f3f1"/>
        </radialGradient>
      </defs>
      <ellipse role="img" aria-label="Kranz aus Anemonen, Rosen, Farn und Eukalyptus rund um den Spruch" cx="220" cy="300" rx="190" ry="262" fill="url(#wreath-tone-a)"/>
      <polygon class="frame-panel" points="210,112 330,172 336,372 252,446 110,406 100,196" fill="var(--panel)"/>
      <polygon class="gold-frame" points="215,80 345,150 352,382 255,472 98,422 88,180" fill="none" stroke="var(--gold)" stroke-width="2"/>
      <polygon class="gold-frame" points="150,118 302,94 388,292 332,442 150,482 68,310" fill="none" stroke="var(--gold)" stroke-width="2"/>
    </svg>
    <p class="cover-quote cover-quote--caps">
      <span>Wake up,</span>
      <span>Make things</span>
      <span>happen!</span>
    </p>
  </section>

  <section class="cover cover--believe">
    <svg class="cover-art" viewBox="0 0 440 606" aria-hidden="false">
      <defs>
        <radialGradient id="wreath-tone-b" cx="50%" cy="50%" r="50%">
          <stop offset="55%" stop-color="#e9ede5"/>
          <stop offset="75%" stop-color="#b9cdb3"/>
          <stop offset="88%" stop-color="#e6d6d0"/>
          <stop offset="100%" stop-color="#f3f3f1"/>
        </radialGradient>
      </defs>
      <ellipse role="img" aria-label="Kranz aus Anemonen, Rosen, Farn und Eukalyptus rund um den Spruch" cx="220" cy="300" rx="190" ry="262" fill="url(#wreath-tone-b)"/>
      <polygon class="frame-panel" points="210,112 330,172 336,372 252,446 110,406 100,196" fill="var(--panel)"/>
      <polygon class="gold-frame" points="215,80 345,150 352,382 255,472 98,422 88,180" fill="none" stroke="var(--gold)" stroke-width="2"/>
      <polygon class="gold-frame" points="150,118 302,94 388,292 332,442 150,482 68,310" fill="none" stroke="var(--gold)" stroke-width="2"/>
    </svg>
    <p class="cover-quote cover-quote--brush">
      <span>believe.</span>
      <span>achieve.</span>
      <span class="quote-word--underlined">succeed.</span>
    </p>
  </section>

</main>
</body>
</html>
```